Letter head / email signature/ contract document templates

We need a professional email signature and letterhead designed for our established carpentry and maintenance company. Our Logo (attached) was originally designed 6 years ago by design guru and we love it, looking for something to compliment it ( not a home job)

```html
<!DOCTYPE html>
<html lang="en">
<head>
<meta charset="utf-8">
<title>Harbour Trim Maintenance – Stationery</title>
<link href="https://fonts.googleapis.com/css2?family=Questrial&display=swap" rel="stylesheet">
<style>
  :root {
    --brand-red: #d42027;
    --ink: #3a3a3c;
    --ink-soft: #555557;
    --paper: #ffffff;
    --backdrop: #e6e6e6;
    --band-grey: #e9eaea;
  }
  * { box-sizing: border-box; margin: 0; padding: 0; }
  html, body {
    width: 830px; height: 1200px; overflow: hidden;
    background: var(--backdrop);
    font-family: "Questrial", "Century Gothic", sans-serif;
    color: var(--ink);
  }
  .canvas { position: relative; width: 830px; height: 1200px; }

  .sheet {
    position: absolute;
    background: var(--paper);
    overflow: hidden;
    box-shadow: 0 1px 3px rgba(0,0,0,0.12);
  }
  .email-signature { left: 111px; top: 74px; width: 610px; height: 154px; }
  .letterhead { left: 110px; top: 270px; width: 611px; height: 856px; }

  /* Brand name block */
  .brand {
    position: absolute;
    display: flex; align-items: center; gap: 6px;
    width: 136px;
    color: var(--ink);
    white-space: nowrap;
  }
  .brand-mark { width: 8px; height: 8px; background: var(--brand-red); flex: none; }
  .brand-name { line-height: 1.05; }
  .brand-name .primary { display: block; font-size: 15px; letter-spacing: 0.3px; }
  .brand-name .secondary { display: block; font-size: 7.5px; letter-spacing: 2.4px; margin-top: 3px; }

  .email-signature .brand { left: 18px; top: 61px; }
  .letterhead .brand { left: 22px; top: 35px; }

  .divider {
    position: absolute; left: 163px; top: 34px;
    width: 1px; height: 83px; background: var(--brand-red);
  }

  .person { position: absolute; left: 173px; top: 38px; }
  .person-name { font-size: 14.5px; color: var(--brand-red); letter-spacing: 0.2px; line-height: 1; }
  .person-role { font-size: 8px; color: var(--ink-soft); margin-top: 2px; }

  .contact-list { position: absolute; list-style: none; }
  .email-signature .contact-list { left: 173px; top: 71px; }
  .letterhead .contact-list { left: 18px; top: 794px; }
  .contact-list li {
    display: flex; align-items: center; gap: 5px;
    font-size: 11px; color: var(--ink-soft); height: 15.2px;
    white-space: nowrap;
  }
  .contact-icon { width: 9px; height: 9px; flex: none; }

  .corner-art {
    position: absolute;
    background: linear-gradient(90deg, var(--band-grey) 0%, var(--brand-red) 35%, var(--brand-red) 100%);
  }
  .email-signature .corner-art { left: 367px; top: 79px; width: 243px; height: 75px; }
  .letterhead .corner-art { left: 225px; top: 738px; width: 386px; height: 118px; }
</style>
</head>
<body>
<div class="canvas">

  <section class="sheet email-signature" aria-label="Email signature">
    <div class="brand">
      <span class="brand-mark"></span>
      <span class="brand-name"><span class="primary">HARBOUR TRIM</span><span class="secondary">MAINTENANCE</span></span>
    </div>
    <div class="divider"></div>
    <div class="person">
      <p class="person-name">JOHN DOE</p>
      <p class="person-role">Manager</p>
    </div>
    <ul class="contact-list">
      <li>
        <svg class="contact-icon" viewBox="0 0 10 10"><circle cx="5" cy="5" r="5" fill="#d42027"/><path d="M3.2 2.6 L4.2 2.5 L4.6 3.8 L4 4.3 Q4.6 5.6 5.8 6.1 L6.3 5.5 L7.5 5.9 L7.4 6.9 Q4.2 7.2 3.2 2.6Z" fill="#fff"/></svg>
        111-222-333
      </li>
      <li>
        <svg class="contact-icon" viewBox="0 0 10 10"><circle cx="5" cy="5" r="5" fill="#d42027"/><rect x="2.6" y="3.3" width="4.8" height="3.4" fill="#fff"/><path d="M2.6 3.3 L5 5.2 L7.4 3.3" stroke="#d42027" stroke-width="0.6" fill="none"/></svg>
        info@harbourtrim.com
      </li>
      <li>
        <svg class="contact-icon" viewBox="0 0 10 10"><circle cx="5" cy="5" r="5" fill="#d42027"/><path d="M5 2.4 L7.4 4.6 L6.8 4.6 L6.8 7.3 L3.2 7.3 L3.2 4.6 L2.6 4.6Z" fill="#fff"/></svg>
        Your address, your city, box 88900
      </li>
    </ul>
    <div class="corner-art" role="img" aria-label="Decorative red house and tool band"></div>
  </section>

  <section class="sheet letterhead" aria-label="Letterhead">
    <div class="brand">
      <span class="brand-mark"></span>
      <span class="brand-name"><span class="primary">HARBOUR TRIM</span><span class="secondary">MAINTENANCE</span></span>
    </div>
    <ul class="contact-list">
      <li>
        <svg class="contact-icon" viewBox="0 0 10 10"><circle cx="5" cy="5" r="5" fill="#d42027"/><path d="M3.2 2.6 L4.2 2.5 L4.6 3.8 L4 4.3 Q4.6 5.6 5.8 6.1 L6.3 5.5 L7.5 5.9 L7.4 6.9 Q4.2 7.2 3.2 2.6Z" fill="#fff"/></svg>
        111-222-333
      </li>
      <li>
        <svg class="contact-icon" viewBox="0 0 10 10"><circle cx="5" cy="5" r="5" fill="#d42027"/><rect x="2.6" y="3.3" width="4.8" height="3.4" fill="#fff"/><path d="M2.6 3.3 L5 5.2 L7.4 3.3" stroke="#d42027" stroke-width="0.6" fill="none"/></svg>
        info@harbourtrim.com
      </li>
      <li>
        <svg class="contact-icon" viewBox="0 0 10 10"><circle cx="5" cy="5" r="5" fill="#d42027"/><path d="M5 2.4 L7.4 4.6 L6.8 4.6 L6.8 7.3 L3.2 7.3 L3.2 4.6 L2.6 4.6Z" fill="#fff"/></svg>
        Your address, your city, box 88900
      </li>
    </ul>
    <div class="corner-art" role="img" aria-label="Decorative red house and tool band"></div>
  </section>

</div>
</body>
</html>
```